Regenerative Medicine Brochure

I want a clean modern bi-fold or tri-fold brochure. We offer non-surgical joint repair for knees, shoulders, and hips. We have many services available including regenerative medicine including stem cell allograft, palatelet rich plasma, prolotherapy, triggerpoint injection, chiropractic and rehab therapies. We are a modern multidisciplinary clinic in coastal California. My logo is already complete and is a vibrant green color. I prefer lots of white space with some areas for service description and what conditions may benefit from the services. Design should convey modern treatments, upscale office and practice, and our target audience is older adults who want to maintain an active pain-free lifestyle.

Target Market(s)

Sports injuries, athletes, seniors who are active, knee pain, shoulder pain, arthritis.

Industry/Entity Type

Alternative Medicine

Font styles to use
Serif

Colors
9bcb3c

Requirements
Must have
• Small white space where we can write date, time, location of next event/class. Colors in brochure to coordinate with logo colors provided.

```html
<!DOCTYPE html>
<html lang="en">
<head>
<meta charset="utf-8">
<title>Tidewell Spine &amp; Joint – Regenerative Medicine Q &amp; A</title>
<link href="https://fonts.googleapis.com/css2?family=Open+Sans:wght@300;400;600;700&display=swap" rel="stylesheet">
<style>
:root{
  --green:#3fb54a;
  --slate:#a9b6c3;
  --slate-dark:#7f8e9d;
  --ink:#3a3a3a;
  --muted:#6b6b6b;
  --paper:#ffffff;
  --backdrop:#dcdcdc;
  --sand:#d9a86a;
  --sky:#e8e3da;
}
*{box-sizing:border-box;margin:0;padding:0}
html,body{width:1200px;height:2392px;overflow:hidden}
body{background:var(--backdrop);font-family:"Open Sans",Arial,sans-serif;color:var(--ink);
  display:flex;flex-direction:column;align-items:center;justify-content:center;gap:150px}
.spread{width:1098px;height:850px;display:grid;grid-template-columns:repeat(3,1fr);
  background:var(--paper);box-shadow:0 14px 40px rgba(0,0,0,.18);position:relative}
.panel{position:relative;overflow:hidden;display:flex;flex-direction:column}
.panel + .panel{border-left:1px solid #eee}
.photo{width:100%}
.text-block{padding:22px 28px 0}
h2{color:var(--green);font-size:17px;font-weight:700;line-height:1.25;margin-bottom:12px}
p{font-size:11.5px;line-height:1.6;color:var(--muted);margin-bottom:11px;text-align:justify}
.green-panel{background:var(--green);color:#fff;align-items:center;text-align:center}
.green-panel p{color:#fff;text-align:justify}
.brand-name{display:flex;align-items:center;gap:10px;font-size:20px;font-weight:600;color:#fff}
.brand-name .dot-mark{width:14px;height:14px;border-radius:50%;background:#fff}
.band{background:var(--slate);color:#fff;font-size:13px;display:flex;align-items:center;justify-content:center;gap:8px}
/* cover */
.cover-brand{display:flex;align-items:center;gap:12px;padding:36px 28px 24px;font-size:22px;font-weight:600;color:var(--ink)}
.cover-brand .dot-mark{width:16px;height:16px;border-radius:50%;background:var(--green)}
.cover-tag{padding:0 28px;margin-top:auto}
.cover-tag .kicker{font-size:13px;letter-spacing:1px;color:var(--slate-dark);text-transform:uppercase}
.cover-tag h1{font-size:21px;font-weight:600;color:var(--ink);margin:6px 0 18px;white-space:nowrap}
/* event form */
.event{width:290px;margin:18px auto 0;text-align:left}
.event label{display:block;font-size:10px;color:rgba(255,255,255,.9);border-bottom:1px solid rgba(255,255,255,.7);padding:10px 4px 4px}
.address{margin-top:auto;font-size:14px;line-height:1.4;padding-bottom:18px}
.phone{font-size:18px;font-weight:600;margin:8px 0 0;display:flex;gap:8px;align-items:center;justify-content:center}
/* areas */
.areas{display:grid;grid-template-columns:repeat(3,80px);gap:10px 18px;margin:10px 0 16px}
.area{display:flex;flex-direction:column;align-items:center;font-size:9px;letter-spacing:.5px;text-transform:uppercase}
.area .joint{width:62px;height:62px;border-radius:50%;background:radial-gradient(circle at 50% 45%,#f07a4a,#2c4f8a 70%);border:2px solid #fff;margin-bottom:4px}
.spread-band{position:absolute;left:0;right:0;bottom:0;height:38px;background:var(--slate);color:#fff;font-size:13px;display:flex;align-items:center;padding-left:28px}
</style>
</head>
<body>

<section class="spread outside">
  <div class="panel flap">
    <div class="photo" role="img" aria-label="Photo of a doctor consulting with a patient at a desk with a stethoscope" style="height:250px;background:linear-gradient(135deg,#eef1f4,#b9c3cc)"></div>
    <div class="text-block">
      <h2>What can I expect from regenerative medicine treatments?</h2>
      <p>During your visit, the team begins with a consultation and physical exam to determine if you're a candidate for regenerative medicine. They ask about your symptoms, condition, overall health and lifestyle. If you're a candidate, the team then explains the procedure and what to expect both during and afterward.</p>
      <p>For the procedure, the team first cleans your skin and applies a topical numbing cream to your skin, if needed. Next, the team injects regenerative products into the treatment area. You may feel a slight pinch or burning sensation during the injection. The visit takes less than thirty minutes and you can return to your usual activities the same day.</p>
      <p>Over the coming weeks and months, the injected products help repair damaged tissues at the treatment site. Most people notice results after two months. Follow-up care may be recommended based on your condition and initial results. Many patients see dramatic results with regenerative medicine treatments, however individual results can vary. Speak to the team to see if regenerative medicine is right for you.</p>
    </div>
  </div>

  <div class="panel green-panel back">
    <div role="img" aria-label="Circular street map showing the clinic location" style="width:170px;height:170px;border-radius:50%;background:radial-gradient(circle,#f7f4ea,#e6e2d6);border:4px solid #fff;margin-top:40px"></div>
    <div class="brand-name" style="margin:26px 0 18px"><span class="dot-mark"></span>Tidewell Spine &amp; Joint</div>
    <div style="padding:0 30px">
      <p>For joint arthritis and muscle pain and injuries, the team at Tidewell Spine &amp; Joint offers minimally invasive regenerative medicine techniques to help you recover from chronic pain. Located in Pismo Bay, California, the medical team utilizes advanced restorative techniques that support the natural healing of injured joints and soft tissues without the need for surgery.</p>
      <p style="text-align:center">To learn more, schedule a consultation online or by phone today.</p>
    </div>
    <div class="phone">
      <svg width="18" height="18" viewBox="0 0 24 24" fill="none" stroke="#fff" stroke-width="2"><circle cx="12" cy="12" r="10"/><path d="M9 7l1.5 3-1.5 1.5a7 7 0 003.5 3.5L14 13.5l3 1.5-1 2.5c-4 0-9-5-9-9z" fill="#fff" stroke="none"/></svg>
      805-555-0142
    </div>
    <div class="event">
      <label>Next event/class:</label>
      <label>Date:</label>
      <label>Location:</label>
    </div>
    <div class="address">2410 Harbor Way<br>Pismo Bay, CA 93499</div>
    <div class="band" style="width:100%;height:38px">www.tidewellspineandjoint.com</div>
  </div>

  <div class="panel cover">
    <div class="cover-brand"><span class="dot-mark"></span>Tidewell Spine &amp; Joint</div>
    <div style="position:relative;height:440px">
      <div role="img" aria-label="Photo of an older couple walking hand in hand along a sunlit beach" style="position:absolute;inset:0;background:linear-gradient(180deg,var(--sky) 0%,#d8cbb5 45%,var(--sand) 100%)"></div>
      <svg style="position:absolute;left:0;bottom:-1px" width="366" height="70" viewBox="0 0 366 70" preserveAspectRatio="none">
        <path d="M0 70 L0 60 Q190 70 366 0 L366 70 Z" fill="#fff"/>
        <path d="M0 60 Q190 70 366 0" fill="none" stroke="var(--green)" stroke-width="4"/>
      </svg>
    </div>
    <div class="cover-tag">
      <div class="kicker">Regenerative Medicine Specialists</div>
      <h1>Regenerative Medicine Q &amp; A</h1>
    </div>
    <div class="band" style="height:38px;font-size:16px;letter-spacing:1px">
      <svg width="16" height="16" viewBox="0 0 24 24" fill="none" stroke="#fff" stroke-width="2"><circle cx="12" cy="12" r="10"/><path d="M9 7l1.5 3-1.5 1.5a7 7 0 003.5 3.5L14 13.5l3 1.5-1 2.5c-4 0-9-5-9-9z" fill="#fff" stroke="none"/></svg>
      805-555-0142
    </div>
  </div>
</section>

<section class="spread inside">
  <div class="panel">
    <div class="photo" role="img" aria-label="Photo of two clinicians reviewing a chart with an older patient" style="height:250px;background:linear-gradient(135deg,#f1f3f5,#9fb4c8)"></div>
    <div class="text-block">
      <h2>What is regenerative medicine?</h2>
      <p>Regenerative medicine is a form of biotechnology that involves injecting regenerative medicine products into injured tissues to help your body repair damage. Regenerative medicine uses tissue engineering techniques to repair muscles, ligaments, cartilage, and tendons damaged by injuries, overuse, and osteoarthritis.</p>
      <p>The medical providers at Tidewell Spine &amp; Joint select from a variety of available treatments and products. These include amniotic allografts, hyaluronic acid, regenerative cells, and cytokines which are powerful growth factors that may help regenerate your own body's tissues.</p>
      <p>After you're injected with the amniotic allograft serum, the growth factors trigger repair at the site of injection. Over the course of the next several weeks, cells grow and multiply forming new tissue.</p>
    </div>
  </div>

  <div class="panel green-panel">
    <div class="brand-name" style="margin:30px 0 16px"><span class="dot-mark"></span>Tidewell Spine &amp; Joint</div>
    <div style="font-size:14px;font-weight:600;padding:0 30px;line-height:1.35">Regenerative medicine may be used in the following areas:</div>
    <div class="areas">
      <div class="area"><div class="joint" role="img" aria-label="Illustration of a painful shoulder joint"></div>Shoulder</div>
      <div class="area"><div class="joint" role="img" aria-label="Illustration of a painful elbow joint"></div>Elbow</div>
      <div class="area"><div class="joint" role="img" aria-label="Illustration of a painful wrist joint"></div>Wrist</div>
      <div class="area"><div class="joint" role="img" aria-label="Illustration of a painful hip joint"></div>Hip</div>
      <div class="area"><div class="joint" role="img" aria-label="Illustration of a painful knee joint"></div>Knee</div>
      <div class="area"><div class="joint" role="img" aria-label="Illustration of a painful ankle joint"></div>Ankle</div>
    </div>
    <div style="padding:0 30px">
      <p>There are many additional types of bone and soft tissue problems, including arthritis, that these injections may benefit.</p>
      <p>With regenerative medicine and amniotic allograft treatments, the team supports the natural healing abilities of your body without the need for drugs or surgical repair and painful recovery. However, not all forms of regenerative medicine are equal.</p>
      <p>At Tidewell Spine &amp; Joint, the team only works with the best regenerative medicine labs to ensure that the right kind of products are selected and that they are of the best quality and highest safety.</p>
    </div>
  </div>

  <div class="panel">
    <div class="text-block" style="padding-top:34px">
      <h2>How does regenerative medicine work?</h2>
      <p>The team uses lab-grade products that are sterilized and processed to inject into the injured area. Once injected, it is thought that these powerful products differentiate into a variety of tissues to trigger your own body to repair damaged tissues. This damage may involve minor tears in muscles, ligaments and tendons, or cartilage and meniscus breakdown in joints.</p>
      <p>Regenerative medicine products contain the basic building blocks of the body's tissues, including proteins, amino acids, and cytokines, responsible for healing and tissue growth. They also provide anti-inflammatory benefits by promoting repair of tissues affected by inflammation.</p>
      <p>While some inflammation is normal and has a benefit in healing injuries, long-term inflammation causes pain, swelling, and further damage to tissues. When you experience too much inflammation, it does more harm than good. Instead of constantly relying on anti-inflammatory medications, regenerative products may be able to correct the problem at the source and reduce the production of natural inflammatory chemicals so you can heal.</p>
    </div>
    <div role="img" aria-label="Photo of a surfer carrying a board out of the ocean at sunset" style="margin-top:auto;margin-bottom:38px;height:210px;background:linear-gradient(180deg,#e9d6d2 0%,#b7a3ad 50%,#6f7f93 100%)"></div>
  </div>

  <div class="spread-band">To learn more, schedule a visit online or by phone at Tidewell Spine &amp; Joint now.</div>
</section>

</body>
</html>
```